Beer Label Design - Tavrin Brewing Company

We lost our chocolate labrador Tavrin of 10 years to cancer last year. In his memory I'm looking for a label design that is created in his image. We are located in San Francisco and he was born (est) 2003. The design will be etched in beer glasses as well. We would like to see designs that have him as the focal point and that look most like him but am not opposed to a more modern take such as the update to the sorvello logo done here: http://brelpax.com/img/sorvello_4.jpg

```html
<!DOCTYPE html>
<html lang="en">
<head>
<meta charset="utf-8">
<title>Tavrin Lager – Label</title>
<link href="https://fonts.googleapis.com/css2?family=Anton&family=Bowlby+One&family=Roboto:wght@700&display=swap" rel="stylesheet">
<style>
  :root {
    --page: #ffffff;
    --sage: #c9cfa4;
    --sage-light: #d6dbb5;
    --stripe-dark: #4a4a48;
    --ribbon: #3c3c3c;
    --ribbon-fold: #5a5a5a;
    --ink: #1c1c1c;
    --orange: #f7931e;
    --orange-deep: #e8700f;
    --art-warm: #e9a04a;
    --art-cool: #8f9479;
  }
  html, body {
    margin: 0;
    width: 1000px;
    height: 1200px;
    overflow: hidden;
    background: var(--page);
  }
  .canvas {
    position: relative;
    width: 1000px;
    height: 1200px;
  }
  .label {
    position: absolute;
    left: 100px;
    top: 36px;
    width: 800px;
    height: 1128px;
    background:
      repeating-linear-gradient(180deg, rgba(255,255,255,0.18) 0 2px, transparent 2px 22px),
      linear-gradient(90deg, var(--stripe-dark) 0%, rgba(201,207,164,0) 22%, rgba(201,207,164,0) 78%, var(--stripe-dark) 100%),
      linear-gradient(180deg, var(--sage-light), var(--sage));
    border: 1px solid #9a9a90;
  }
  .label-art {
    position: absolute;
    inset: 0;
    width: 800px;
    height: 1128px;
  }
  .banner-text {
    font-family: "Anton", "Impact", sans-serif;
    font-size: 62px;
    fill: var(--orange);
    letter-spacing: 1px;
  }
  .brand-name {
    font-family: "Bowlby One", "Arial Black", sans-serif;
    font-size: 100px;
    fill: var(--ink);
  }
  .style-name {
    font-family: "Bowlby One", "Arial Black", sans-serif;
    font-size: 140px;
    fill: var(--orange);
  }
  .fine-print {
    font-family: "Roboto", "Arial", sans-serif;
    font-weight: 700;
    font-size: 30px;
    fill: var(--ink);
  }
</style>
</head>
<body>
<main class="canvas">
  <section class="label">
    <svg class="label-art" viewBox="0 0 800 1128" xmlns="http://www.w3.org/2000/svg">
      <defs>
        <linearGradient id="mascot-tones" x1="0" y1="0" x2="1" y2="1">
          <stop offset="0" stop-color="var(--art-warm)"/>
          <stop offset="0.6" stop-color="#b0743e"/>
          <stop offset="1" stop-color="var(--art-cool)"/>
        </linearGradient>
        <linearGradient id="hop-tones" x1="0" y1="0" x2="0" y2="1">
          <stop offset="0" stop-color="var(--orange)"/>
          <stop offset="1" stop-color="var(--orange-deep)"/>
        </linearGradient>
        <path id="brand-arc" d="M 120 770 Q 400 700 680 770"/>
      </defs>

      <g class="top-ribbon">
        <polygon points="120,40 150,40 150,170 120,150" fill="var(--ribbon-fold)"/>
        <polygon points="680,40 650,40 650,170 680,150" fill="var(--ribbon-fold)"/>
        <polygon points="142,18 658,18 658,148 400,164 142,148" fill="var(--ribbon)"/>
        <text class="banner-text" x="400" y="118" text-anchor="middle" textLength="470" lengthAdjust="spacingAndGlyphs">SUPER PREMIUM BEER</text>
      </g>

      <rect class="mascot-art" x="150" y="180" width="530" height="410" rx="30"
            fill="url(#mascot-tones)" opacity="0.85"
            role="img" aria-label="Illustration of a chocolate labrador superhero in an orange suit and cape, holding a beer mug and flying over a suspension bridge"/>

      <g class="brand-arch">
        <path d="M 96 668 Q 400 560 704 668" fill="none" stroke="var(--orange)" stroke-width="7"/>
        <path d="M 96 680 Q 400 574 704 680" fill="none" stroke="var(--ink)" stroke-width="3"/>
        <text class="brand-name" textLength="520" lengthAdjust="spacingAndGlyphs">
          <textPath href="#brand-arc" startOffset="50%" text-anchor="middle">TAVRIN</textPath>
        </text>
        <path d="M 96 800 Q 400 700 704 800" fill="none" stroke="var(--orange)" stroke-width="7"/>
      </g>

      <g class="style-ribbon">
        <polygon points="142,832 658,814 662,968 400,982 138,968" fill="var(--ink)"/>
        <text class="style-name" x="400" y="950" text-anchor="middle" textLength="460" lengthAdjust="spacingAndGlyphs">LAGER</text>
      </g>

      <rect class="hop-art" x="286" y="978" width="242" height="82" rx="36"
            fill="url(#hop-tones)"
            role="img" aria-label="Three orange hop cones in a row"/>

      <text class="fine-print" x="71" y="1100">600 ml</text>
      <text class="fine-print" x="740" y="1100" text-anchor="end">4.0% Avb</text>
    </svg>
  </section>
</main>
</body>
</html>
```